General Dental Office Business Card

I run a private general dental office in southern California, and would like a refresh/redesign of my business card. I focus on quality care rather than volume. The email address on the uploaded current card should be updated to: info@maplecovedental.example. The current card's logo is a deboss, but I am open to other ideas. The logo can be refreshed, but it is something that's been with me since the beginning of the office, so I wouldn't want a drastic redesign.
Target Market(s)
Adults 18-99, whoever needs dental services
Industry/Entity Type
Healthcare/Dental
Contact Information for Business Card
Name, Address, Phone, email
Colors
Designer to choose colors to be used in the design.
Requirements
Must have
- Logo (Same as original one in the uploaded file), space on back for appointment time/date

```html
<!DOCTYPE html>
<html lang="en">
<head>
<meta charset="utf-8">
<title>Maple Cove Dental – Business Card</title>
<link href="https://fonts.googleapis.com/css2?family=Red+Hat+Display:wght@400;500&display=swap" rel="stylesheet">
<style>
  :root {
    --teal: #2eb6c4;
    --white: #ffffff;
    --backdrop: #e9e9ea;
    --mark-faint: rgba(255, 255, 255, 0.35);
  }
  * { margin: 0; padding: 0; box-sizing: border-box; }
  html, body { width: 1200px; height: 675px; overflow: hidden; }
  body {
    position: relative;
    background: var(--backdrop);
    font-family: "Red Hat Display", sans-serif;
  }
  .card {
    position: absolute;
    width: 420px;
    height: 240px;
    box-shadow: 0 2px 6px rgba(0, 0, 0, 0.18);
  }
  .card-front { left: 160px; top: 97px; background: var(--teal); color: var(--white); }
  .card-back { left: 619px; top: 337px; background: var(--white); color: var(--teal); }

  .front-mark {
    position: absolute;
    left: 43px; top: 56px;
    width: 110px; height: 110px;
    border: 4px solid var(--mark-faint);
    border-radius: 50%;
  }
  .dentist {
    position: absolute;
    right: 18px; top: 30px;
    text-align: right;
  }
  .dentist-name { font-size: 25px; font-weight: 500; letter-spacing: -0.3px; line-height: 1.1; }
  .dentist-title { font-size: 12.5px; font-weight: 400; margin-top: 6px; }

  .practice {
    position: absolute;
    left: 210px; top: 113px;
  }
  .practice-name { font-size: 12.5px; font-weight: 500; letter-spacing: 0.2px; margin-bottom: 9px; }
  .contact-list { list-style: none; }
  .contact-item {
    display: flex; align-items: center;
    font-size: 8px; line-height: 1.3;
    margin-bottom: 8.5px;
  }
  .contact-item svg { width: 9px; height: 9px; margin-right: 9px; flex: none; fill: var(--white); }

  .brand {
    position: absolute;
    left: 83px; top: 27px;
    display: flex; align-items: center;
  }
  .brand-dot {
    width: 66px; height: 66px;
    border: 3px solid var(--teal);
    border-radius: 50%;
    margin-right: 9px;
  }
  .brand-name { font-size: 27px; font-weight: 500; line-height: 1.15; }

  .appointment {
    position: absolute;
    left: 57px; top: 160px;
    font-size: 12px;
  }
  .appointment-line { display: flex; align-items: flex-end; margin-bottom: 12px; }
  .blank { display: inline-block; border-bottom: 1px solid var(--teal); margin-left: 4px; height: 12px; }
  .blank-date { width: 116px; }
  .blank-time { width: 117px; }
</style>
</head>
<body>
  <section class="card card-front">
    <div class="front-mark" aria-hidden="true"></div>
    <div class="dentist">
      <div class="dentist-name">Daniel R. Moreno DDS</div>
      <div class="dentist-title">General Dentistry</div>
    </div>
    <div class="practice">
      <div class="practice-name">MAPLE COVE DENTAL</div>
      <ul class="contact-list">
        <li class="contact-item">
          <svg viewBox="0 0 24 24"><path d="M6.6 10.8a15.1 15.1 0 0 0 6.6 6.6l2.2-2.2c.3-.3.7-.4 1-.2 1.1.4 2.3.6 3.6.6.6 0 1 .4 1 1V20c0 .6-.4 1-1 1A17 17 0 0 1 3 4c0-.6.4-1 1-1h3.5c.6 0 1 .4 1 1 0 1.3.2 2.5.6 3.6.1.3 0 .7-.2 1z"/></svg>
          949-555-0142
        </li>
        <li class="contact-item">
          <svg viewBox="0 0 24 24"><path d="M20 4H4a2 2 0 0 0-2 2v12a2 2 0 0 0 2 2h16a2 2 0 0 0 2-2V6a2 2 0 0 0-2-2zm0 4-8 5-8-5V6l8 5 8-5z"/></svg>
          info@maplecovedental.example
        </li>
        <li class="contact-item">
          <svg viewBox="0 0 24 24"><path d="M12 2a7 7 0 0 0-7 7c0 5.2 7 13 7 13s7-7.8 7-13a7 7 0 0 0-7-7zm0 9.5A2.5 2.5 0 1 1 12 6.5a2.5 2.5 0 0 1 0 5z"/></svg>
          <span>1280 Harbor Crest Way<br>Laguna Vista, CA 92690</span>
        </li>
        <li class="contact-item">
          <svg viewBox="0 0 24 24"><path d="M12 2a10 10 0 1 0 0 20 10 10 0 0 0 0-20zm6.9 6h-2.9a15.7 15.7 0 0 0-1.4-3.6A8 8 0 0 1 18.9 8zM12 4c.8 1.2 1.5 2.5 1.9 4h-3.8c.4-1.4 1.1-2.8 1.9-4zM4.3 14a8.2 8.2 0 0 1 0-4h3.4a16.5 16.5 0 0 0 0 4zm.8 2h2.9c.3 1.3.8 2.5 1.4 3.6A8 8 0 0 1 5.1 16zM8 8H5.1a8 8 0 0 1 4.3-3.6C8.8 5.5 8.3 6.7 8 8zm4 12c-.8-1.2-1.5-2.5-1.9-4h3.8c-.4 1.4-1.1 2.8-1.9 4zm2.3-6H9.7a14.7 14.7 0 0 1 0-4h4.6a14.7 14.7 0 0 1 0 4zm.3 5.6c.6-1.1 1.1-2.3 1.4-3.6h2.9a8 8 0 0 1-4.3 3.6zm1.7-5.6a16.5 16.5 0 0 0 0-4h3.4a8.2 8.2 0 0 1 0 4z"/></svg>
          www.maplecovedental.example
        </li>
      </ul>
    </div>
  </section>

  <section class="card card-back">
    <div class="brand">
      <div class="brand-dot" aria-hidden="true"></div>
      <div class="brand-name">MAPLE COVE<br>DENTAL</div>
    </div>
    <div class="appointment">
      <div class="appointment-line">Appointment Date :<span class="blank blank-date"></span></div>
      <div class="appointment-line">Time :<span class="blank blank-time"></span></div>
    </div>
  </section>
</body>
</html>
```